Aviation Banner Ad Designs

SkyLedgerMetrics provides access to the most accurate aircraft operating cost information, to compare Piston, Turboprop and Jet aircraft.

The banners ads will be used for retargeting/remarketing - to bring visitors back to the site. The banners should remind and reinforce the key messages of what the site provides.

Target Market(s)

Private aircraft buyers including:
- Aircraft Brokers
- Charter Operators
- Corporate Flight Departments
- Aircraft Management companies
- Financial Institutions
- Aircraft Owners
- Prospective Buyers

Requirements
Must have
• A. Banner Objective
The visual and textual content of the banner should remind the viewer about the features of the site, and prompt them to return to the site.
1. Arresting visual
2. Headline
3. Single message
4. Compelling CTA
5. Logo - big enough to see
6. Standard DWR ad sizes/specs

B. Design Elements
Logo: As attached
Main Title: Calculate Jet Operating Costs
Subtitle: Compare Ownership Usage Scenarios
Call to Action Button: Compare Ownership Costs
Background: Several images supplied as options

C. Banner Sizes
Do examples as 300×250 , 728×90 , 160×600
Final sizes to also include 320×100 , 336x280 , 300x600

Finally delivery as .jpg files.

Font - use same font as on site

```html
<!DOCTYPE html>
<html lang="en">
<head>
<meta charset="utf-8">
<title>SkyLedgerMetrics – Calculate Jet Operating Costs</title>
<link rel="stylesheet" href="https://fonts.googleapis.com/css2?family=Arimo:wght@400;700&display=swap">
<style>
  :root {
    --page-bg: #e4e4e4;
    --sky-top: #8797ab;
    --sky-mid: #b9b8b6;
    --sky-haze: #dccbb8;
    --sky-glow: #e3b07e;
    --sky-low: #d9a070;
    --jet-light: #c9c6c2;
    --jet-mid: #8d8a87;
    --jet-dark: #4d4a48;
    --ink: #0d0d0d;
    --cta-bg: #054c86;
    --cta-ink: #ffffff;
  }
  * { box-sizing: border-box; margin: 0; padding: 0; }
  html, body {
    width: 1200px;
    height: 800px;
    overflow: hidden;
    background: var(--page-bg);
    font-family: "Arimo", Arial, sans-serif;
  }
  .canvas {
    position: relative;
    width: 1200px;
    height: 800px;
  }
  .banner {
    position: absolute;
    left: 420px;
    top: 40px;
    width: 360px;
    height: 720px;
    overflow: hidden;
  }
  .banner-sky {
    position: absolute;
    inset: 0;
    background: linear-gradient(180deg,
      var(--sky-top) 0%,
      var(--sky-mid) 30%,
      var(--sky-haze) 55%,
      var(--sky-glow) 78%,
      var(--sky-low) 100%);
  }
  .banner-jet {
    position: absolute;
    left: 0;
    top: 224px;
    width: 360px;
    height: 176px;
    background:
      radial-gradient(ellipse 62% 34% at 48% 52%, var(--jet-light) 0%, var(--jet-mid) 55%, rgba(77, 74, 72, 0) 100%),
      linear-gradient(160deg, rgba(77, 74, 72, 0.35) 0%, rgba(141, 138, 135, 0.25) 60%, rgba(201, 198, 194, 0) 100%);
  }
  .brand {
    position: absolute;
    left: 14px;
    top: 46px;
    display: flex;
    align-items: center;
    gap: 12px;
  }
  .brand-mark {
    width: 34px;
    height: 34px;
    background: var(--ink);
  }
  .brand-name {
    font-size: 28px;
    font-weight: 700;
    color: var(--ink);
    letter-spacing: 0.5px;
  }
  .subtitle {
    position: absolute;
    left: 0;
    top: 148px;
    width: 100%;
    text-align: center;
    font-size: 21px;
    font-weight: 400;
    line-height: 27px;
    letter-spacing: 1.8px;
    color: var(--ink);
    text-transform: uppercase;
  }
  .headline {
    position: absolute;
    left: 0;
    top: 416px;
    width: 100%;
    text-align: center;
    font-size: 44px;
    font-weight: 700;
    line-height: 52px;
    letter-spacing: -1.5px;
    color: var(--ink);
    text-transform: uppercase;
  }
  .cta {
    position: absolute;
    left: 0;
    bottom: 0;
    width: 100%;
    height: 55px;
    background: var(--cta-bg);
    color: var(--cta-ink);
    display: flex;
    align-items: center;
    justify-content: center;
    font-size: 16.5px;
    font-weight: 400;
    letter-spacing: 1.5px;
    text-transform: uppercase;
  }
</style>
</head>
<body>
  <main class="canvas">
    <section class="banner">
      <div class="banner-sky" role="img" aria-label="Sunset sky with grey clouds above and glowing orange clouds below"></div>
      <div class="banner-jet" role="img" aria-label="Business jet climbing after takeoff with landing gear down"></div>
      <div class="brand">
        <span class="brand-mark"></span>
        <span class="brand-name">SkyLedgerMetrics</span>
      </div>
      <p class="subtitle">Compare Ownership<br>Usage Scenarios</p>
      <h1 class="headline">Calculate<br>Jet<br>Operating<br>Costs</h1>
      <div class="cta">Compare Ownership Costs</div>
    </section>
  </main>
</body>
</html>
```